Business Card Design for Small Electrical Contractor

I need to update my business card into something a little more modern. We are a small electrical contracting company. We service domestic and commercial places around Sydney. We have 2 logo designs at the moment. I have uploaded both and 2 different sizes to work with.

Industry/Entity Type

Business

Contact Information for Business Card

Leo Hartigan
8/21-23 Birch Rd, Kelsworth 2087
t - (02) 9381 4720
m - 0427 815 903
E - info@hartiganelx.com.au
W - hartiganelx.com.au
ABN: 42 907 551 316

Font styles to use
Sans Serif

Requirements
Must have
• I would also like to see the below fit on somewhere aswell
• - Licensed Electrician
• - Level 2 (Cat 1 & 4)
• - Domestic
• - Commercial
• - Repairs and Installations
• - Data
Nice to have
• Try and keep similar colours as logo
Should not have
• No lightning bolts or light globes. Smart and professional please.

```html
<!DOCTYPE html>
<html lang="en">
<head>
<meta charset="utf-8">
<title>L&amp;K Hartigan Electrical – Business Card</title>
<link href="https://fonts.googleapis.com/css2?family=Montserrat:wght@400;500;600;700&display=swap" rel="stylesheet">
<style>
  :root {
    --bg: #d9d9d9;
    --card-black: #0b0b0b;
    --card-white: #ffffff;
    --orange: #f7941d;
    --green: #1f3b2d;
    --text-light: #f2f2f2;
  }
  * { box-sizing: border-box; margin: 0; padding: 0; }
  html, body { width: 1200px; height: 900px; overflow: hidden; }
  body {
    background: var(--bg);
    font-family: "Montserrat", sans-serif;
    position: relative;
  }
  .card {
    position: absolute;
    left: 270px;
    width: 660px;
    height: 380px;
    border-radius: 22px;
    overflow: hidden;
    background: var(--card-black);
    color: var(--text-light);
  }
  .card--front { top: 50px; }
  .card--back { top: 470px; }

  /* Front */
  .front-brand {
    position: absolute;
    top: 70px;
    left: 0; right: 0;
    text-align: center;
  }
  .brand-name {
    font-size: 34px;
    font-weight: 700;
    letter-spacing: 1px;
    color: var(--card-white);
  }
  .brand-rule {
    width: 330px;
    height: 2px;
    background: var(--orange);
    margin: 14px auto 0;
  }
  .services {
    position: absolute;
    top: 158px;
    left: 0; right: 0;
    list-style: none;
    text-align: center;
    font-size: 15px;
    line-height: 19px;
    font-weight: 400;
  }
  .front-web {
    position: absolute;
    bottom: 40px;
    left: 0; right: 0;
    text-align: center;
    font-size: 16px;
    font-weight: 500;
  }
  .front-web .accent { color: var(--orange); }

  /* Back */
  .back-panel {
    position: absolute;
    left: 0; top: 0; bottom: 0;
    width: 190px;
    background: var(--card-white);
  }
  .back-panel-rule {
    position: absolute;
    left: 200px; top: 0; bottom: 0;
    width: 2px;
    background: var(--orange);
  }
  .back-brand {
    position: absolute;
    left: 95px;
    top: 190px;
    transform: translate(-50%, -50%) rotate(-90deg);
    white-space: nowrap;
    font-size: 28px;
    font-weight: 700;
    color: var(--green);
    letter-spacing: 1px;
  }
  .corner-mark {
    position: absolute;
    top: 28px;
    right: 26px;
  }
  .contact {
    position: absolute;
    right: 70px;
    top: 60px;
    text-align: right;
    font-size: 16px;
    line-height: 24px;
  }
  .contact-name {
    font-size: 24px;
    font-weight: 700;
    margin-bottom: 6px;
  }
  .contact-name .first { color: var(--orange); }
  .label { color: var(--orange); }
  .contact-icons {
    position: absolute;
    right: 38px;
    top: 172px;
    display: flex;
    flex-direction: column;
  }
  .contact-icons svg { width: 16px; height: 16px; margin: 4px 0; }
  .contact .gap { height: 10px; }
</style>
</head>
<body>

<section class="card card--front">
  <div class="front-brand">
    <div class="brand-name">L&amp;K Hartigan Electrical</div>
    <div class="brand-rule"></div>
  </div>
  <ul class="services">
    <li>Licensed Electrician</li>
    <li>Level 2 (Cat 1 &amp; 4)</li>
    <li>Domestic</li>
    <li>Commercial</li>
    <li>Repairs and Installations</li>
    <li>Data</li>
  </ul>
  <div class="front-web">www.<span class="accent">hartiganelx</span>.com.au</div>
</section>

<section class="card card--back">
  <div class="back-panel">
    <div class="back-brand">L&amp;K Hartigan Electrical</div>
  </div>
  <div class="back-panel-rule"></div>

  <svg class="corner-mark" width="34" height="24" viewBox="0 0 34 24" aria-hidden="true">
    <polygon points="0,0 34,0 17,24" fill="var(--orange)"/>
  </svg>

  <div class="contact">
    <div class="contact-name"><span class="first">Leo</span> Hartigan</div>
    <div>8/21-23 Birch Rd</div>
    <div>Kelsworth 2087</div>
    <div><span class="label">ABN:</span> 42 907 551 316</div>
    <div>(02) 9381 4720</div>
    <div>0427 815 903</div>
    <div>info@hartiganelx.com.au</div>
    <div>www.hartiganelx.com.au</div>
  </div>

  <div class="contact-icons" aria-hidden="true">
    <svg viewBox="0 0 16 16"><path d="M4 2l2.5 3-1.5 1.5c.8 1.8 2.2 3.2 4 4L10.5 9 13.5 11.5 12 14C7 13.5 2.5 9 2 4z" fill="var(--orange)"/></svg>
    <svg viewBox="0 0 16 16"><rect x="4.5" y="1.5" width="7" height="13" rx="1.5" fill="none" stroke="var(--orange)" stroke-width="1.6"/><circle cx="8" cy="12" r="0.9" fill="var(--orange)"/></svg>
    <svg viewBox="0 0 16 16"><rect x="1.5" y="3.5" width="13" height="9" rx="1" fill="none" stroke="var(--orange)" stroke-width="1.6"/><path d="M2 4l6 5 6-5" fill="none" stroke="var(--orange)" stroke-width="1.4"/></svg>
    <svg viewBox="0 0 16 16"><circle cx="8" cy="8" r="6.3" fill="none" stroke="var(--orange)" stroke-width="1.5"/><ellipse cx="8" cy="8" rx="2.8" ry="6.3" fill="none" stroke="var(--orange)" stroke-width="1.2"/><path d="M1.8 8h12.4" stroke="var(--orange)" stroke-width="1.2"/></svg>
  </div>
</section>

</body>
</html>
```